Quick Straightforward Billboard Redesign

- Design billboard sized for 10 foot' x 36' foot width live area size and please include bleeds 6" around all sides
- Exact blue color match is imperative in headline, logo, phone number bubble or wherever used. C-83 / M-45 / Y-1 / K-0-
- What I hope to illustrate is that our company offers the best porch screening in the area area, in regards to quality, expertise, durability, storms proof, but we do not build screen porches.
- Current board is attached below from previous designer, and as you can see sizing was off, white space on edges make it appear to be sized incorrectly.
- I also attached my own little mock up idea well well if it helps, favorite image, logo, headline, etc and ideas perhaps on expanding or making this better?

Thanks so much!

Target Market(s)

Drivers and passengers, Southeastern NC, are of immense new construction and high end homes.

Industry/Entity Type

Construction

Colors
0054AA
0677BA
7BADD7
CADEEF
E8F1F8

Requirements
Must have
• Blue color matching
Nice to have
• Design spins or other thoughts on my little mock up

```html
<!DOCTYPE html>
<html lang="en">
<head>
<meta charset="utf-8">
<title>Tidewater Screening Billboard</title>
<link rel="stylesheet" href="https://fonts.googleapis.com/css2?family=Barlow+Condensed:wght@500;600&display=swap">
<style>
  :root {
    --brand-blue: #2e8ff0;
    --accent-green: #3ee83a;
    --paper: #ffffff;
    --sky: #7badd7;
    --sky-light: #cadeef;
    --ceiling: #f4f7f9;
    --lawn: #8fcf6a;
    --water: #a9c7de;
  }
  * { margin: 0; padding: 0; box-sizing: border-box; }
  html, body { width: 1200px; height: 333px; overflow: hidden; background: var(--paper); }
  .billboard {
    position: relative;
    width: 1200px;
    height: 333px;
    background: var(--paper);
    font-family: "Barlow Condensed", "Arial Narrow", sans-serif;
    overflow: hidden;
  }
  .porch-photo {
    position: absolute;
    left: 690px;
    top: 0;
    width: 510px;
    height: 333px;
    background:
      linear-gradient(180deg, var(--ceiling) 0%, var(--ceiling) 30%, var(--sky) 31%, var(--sky-light) 45%, var(--water) 52%, var(--lawn) 60%, #b7c7a0 72%, #e6e2da 80%, #d9d6d0 100%);
    -webkit-mask-image: linear-gradient(90deg, transparent 0%, #000 22%);
    mask-image: linear-gradient(90deg, transparent 0%, #000 22%);
  }
  .headline, .tagline, .brand-name {
    position: absolute;
    line-height: 1;
    font-weight: 600;
    white-space: nowrap;
    transform-origin: left top;
  }
  .headline {
    left: 64px;
    top: 8px;
    font-size: 124px;
    letter-spacing: -1px;
    color: var(--brand-blue);
    transform: scaleX(0.87);
  }
  .tagline {
    left: 65px;
    top: 125px;
    font-size: 76px;
    letter-spacing: -0.5px;
    color: var(--accent-green);
    transform: scaleX(0.86);
  }
  .brand-mark {
    position: absolute;
    left: 67px;
    top: 247px;
    width: 52px;
    height: 52px;
    background: var(--brand-blue);
  }
  .brand-name {
    left: 139px;
    top: 254px;
    font-size: 51px;
    color: var(--brand-blue);
    text-transform: uppercase;
    letter-spacing: -0.5px;
    transform: scaleX(0.8);
  }
  .phone {
    position: absolute;
    left: 487px;
    top: 237px;
    width: 258px;
    height: 63px;
    border-radius: 24px 24px 24px 0;
    background: var(--brand-blue);
    color: var(--paper);
    font-size: 54px;
    font-weight: 600;
    line-height: 63px;
    text-align: center;
    letter-spacing: -0.5px;
  }
</style>
</head>
<body>
  <main class="billboard">
    <div class="porch-photo" role="img" aria-label="Covered screened porch with wicker seating, ceiling fan and potted palm overlooking a lawn and lake"></div>
    <h1 class="headline">Screen Your Porch</h1>
    <p class="tagline">Built for the Coast</p>
    <span class="brand-mark"></span>
    <span class="brand-name">Tidewater Screening</span>
    <p class="phone">910.555.0148</p>
  </main>
</body>
</html>
```